Group fitness classes - DL flyer

We need a flyer design for our boutique fitness studio.

We would prefer to see the use of pictures in the design.

One sided. Please allow space around the edges for bleed.

Flyer should have the following text:

Harwell Motion Loft
Group fitness special – two weeks unlimited group fitness classes for $29*
Enjoy unlimited access to our fantastic group classes including PulseRun, Yoga, Strength Circuit and Self Defence Martial Arts.
Purchase your pass through our online store by selecting the "Special Offers" option.
Bring this flyer to your first class and receive an extra two weeks free!

www.harwellmotionloft.com.au
or phone
0482 *** ***
4/63 Birchwood Lane Kestrel Park

*New clients only

Industry/Entity Type

Boutique

Font styles to use
Serif
Sans Serif

Requirements
Must have
• Photos
Should not have
• Cartoons

```html
<!DOCTYPE html>
<html lang="en">
<head>
<meta charset="utf-8">
<title>Harwell Motion Loft – Group Fitness DL Flyer</title>
<link rel="stylesheet" href="https://fonts.googleapis.com/css2?family=Oswald:wght@500;600&family=Roboto:wght@300;400&display=swap">
<style>
  :root {
    --backdrop: #ece9e4;
    --paper: #ffffff;
    --brand-red: #a3161c;
    --banner-red-light: #d0342f;
    --banner-red-dark: #8e1a1e;
    --bar-red: #7b1419;
    --swoosh-grey: #c9c9c9;
    --ink: #1c1c1c;
    --white: #ffffff;
    --photo-top: #b8a89c;
    --photo-mid: #3fc1c0;
    --photo-low: #8a5a3c;
  }
  * { margin: 0; padding: 0; box-sizing: border-box; }
  html, body {
    width: 1200px; height: 2513px; overflow: hidden;
    background: var(--backdrop);
  }
  .flyer {
    position: absolute; left: 75px; top: 75px;
    width: 1051px; height: 2364px;
    background: var(--paper);
    overflow: hidden;
    font-family: "Roboto", Arial, sans-serif;
    color: var(--ink);
  }
  .flyer-shapes { position: absolute; inset: 0; }
  .offer-headline {
    position: absolute; right: 66px; top: 955px;
    text-align: right; color: var(--white);
  }
  .offer-title {
    font-family: "Oswald", "Arial Narrow", sans-serif;
    font-weight: 600; font-size: 88px; line-height: 1.05;
  }
  .offer-sub {
    font-family: "Roboto", Arial, sans-serif;
    font-weight: 300; font-size: 58px; line-height: 1.08;
  }
  .offer-price {
    font-family: "Oswald", "Arial Narrow", sans-serif;
    font-weight: 600; font-size: 90px; line-height: 1.1;
  }
  .offer-details {
    position: absolute; left: 90px; right: 90px; top: 1400px;
    text-align: center;
  }
  .detail-copy { font-size: 30px; line-height: 1.35; }
  .detail-highlight {
    font-family: "Oswald", "Arial Narrow", sans-serif;
    font-weight: 500; color: var(--brand-red);
    font-size: 38px; line-height: 1.3;
  }
  .detail-tail {
    font-family: "Roboto", Arial, sans-serif;
    font-weight: 400; font-size: 30px; color: var(--ink);
  }
  .offer-details .detail-copy + .detail-highlight { margin-top: 4px; }
  .offer-details .detail-highlight + .detail-copy { margin-top: 16px; }
  .contact-block { margin-top: 10px; }
  .contact-line {
    font-family: "Oswald", "Arial Narrow", sans-serif;
    font-weight: 500; color: var(--brand-red);
    font-size: 40px; line-height: 1.65;
  }
  .studio-name {
    position: absolute; left: 0; right: 0; top: 2060px;
    text-align: center;
    font-family: "Oswald", "Arial Narrow", sans-serif;
    font-weight: 500; font-size: 60px; color: var(--brand-red);
    letter-spacing: 2px; text-transform: uppercase;
  }
  .address-bar {
    position: absolute; left: 63px; width: 920px; top: 2242px; height: 122px;
    background: var(--bar-red);
    border-radius: 26px 26px 0 0;
    color: var(--white);
    font-size: 44px; font-weight: 400;
    display: flex; align-items: center; justify-content: center;
  }
</style>
</head>
<body>
<main class="flyer">
  <svg class="flyer-shapes" width="1051" height="2364" viewBox="0 0 1051 2364">
    <defs>
      <linearGradient id="photoTone" x1="0" y1="0" x2="0.3" y2="1">
        <stop offset="0" stop-color="var(--photo-top)"/>
        <stop offset="0.55" stop-color="var(--photo-mid)"/>
        <stop offset="1" stop-color="var(--photo-low)"/>
      </linearGradient>
      <linearGradient id="bannerTone" x1="0" y1="0" x2="1" y2="1">
        <stop offset="0" stop-color="var(--banner-red-light)"/>
        <stop offset="1" stop-color="var(--banner-red-dark)"/>
      </linearGradient>
    </defs>
    <path class="swoosh-grey" d="M0 640 C80 900 260 1020 520 1010 C700 1000 880 960 1051 960 V1040 C860 1030 680 1080 500 1080 C230 1080 60 930 0 780 Z" fill="var(--swoosh-grey)"/>
    <path class="swoosh-red" d="M0 600 C80 860 260 980 520 975 C700 970 880 930 1051 930 V990 C860 985 690 1030 510 1035 C240 1040 60 890 0 720 Z" fill="var(--banner-red-dark)"/>
    <path class="class-photo" role="img" aria-label="Photo of smiling women doing sit-ups in a group fitness class, instructor with headset in front"
      d="M0 0 H1051 V920 C880 915 700 955 520 950 C260 945 90 820 0 580 Z" fill="url(#photoTone)"/>
    <path class="banner-outline" d="M1051 900 C880 880 620 890 450 950 C320 995 300 1090 330 1170 C370 1270 520 1325 720 1325 C860 1325 960 1310 1051 1295 Z" fill="var(--swoosh-grey)"/>
    <path class="banner" d="M1051 925 C880 905 630 915 470 970 C345 1012 330 1095 355 1165 C390 1255 525 1300 720 1300 C860 1300 960 1288 1051 1272 Z" fill="url(#bannerTone)"/>
  </svg>

  <div class="offer-headline">
    <div class="offer-title">Group fitness</div>
    <div class="offer-sub">two weeks unlimited<br>fitness classes for</div>
    <div class="offer-price">$29*</div>
  </div>

  <section class="offer-details">
    <p class="detail-copy">Enjoy unlimited access to our fantastic group classes including</p>
    <p class="detail-highlight">PulseRun, Yoga, Strength Circuit and Self Defence<br>Martial Arts.</p>
    <p class="detail-copy">Purchase your pass through our online store by selecting the</p>
    <p class="detail-highlight">"Special Offers" <span class="detail-tail">option.</span></p>
    <p class="detail-copy">Bring this flyer to your first class and receive an extra two weeks<br>free!</p>
    <div class="contact-block">
      <p class="contact-line">www.harwellmotionloft.com.au</p>
      <p class="contact-line">or phone : 0482 *** ***</p>
      <p class="contact-line">*New clients only</p>
    </div>
  </section>

  <div class="studio-name">Harwell Motion Loft</div>

  <footer class="address-bar">4/63 Birchwood Lane Kestrel Park</footer>
</main>
</body>
</html>
```